Copper lark buildworks

Copper lark buildworks is a small construction company.
Who is a licenced builder, Carpenter, joiner,
working on heritage ,new build, speacial projects and sometimes furniture

Industry/Entity Type

Construction

```html
<!DOCTYPE html>
<html lang="en">
<head>
<meta charset="utf-8">
<title>Copper lark buildworks – business card</title>
<link rel="stylesheet" href="https://fonts.googleapis.com/css2?family=Montserrat:wght@400;600;800&display=swap">
<style>
  :root {
    --page-bg: #e6e8eb;
    --card-dark: #0b0b0b;
    --card-mid: #242424;
    --brand-green: #6cc04a;
    --brand-green-deep: #3f9a2c;
    --ring-light: #f2f2f2;
    --text-light: #ffffff;
  }
  * { margin: 0; padding: 0; box-sizing: border-box; }
  html, body { width: 828px; height: 1200px; overflow: hidden; }
  body {
    background: var(--page-bg);
    font-family: "Montserrat", Arial, sans-serif;
    position: relative;
  }
  .card {
    position: absolute;
    left: 64px;
    width: 700px;
    height: 400px;
    border-radius: 22px;
    overflow: hidden;
    background: linear-gradient(135deg, var(--card-mid) 0%, var(--card-dark) 60%);
    box-shadow: 0 12px 30px rgba(0,0,0,0.25);
  }
  .card--front { top: 130px; }
  .card--back { top: 670px; }

  /* front */
  .front__band {
    position: absolute;
    right: 0; top: 0;
    width: 190px; height: 100%;
    background: linear-gradient(180deg, var(--brand-green) 0%, var(--brand-green-deep) 100%);
  }
  .front__emblem {
    position: absolute;
    left: 372px; top: 62px;
    width: 276px; height: 276px;
    border-radius: 50%;
    background: var(--card-dark);
    border: 12px solid var(--ring-light);
  }
  .front__brand {
    position: absolute;
    left: 48px; top: 62px;
  }
  .brand-name {
    font-weight: 800;
    color: var(--brand-green);
    text-transform: uppercase;
    line-height: 1.1;
  }
  .brand-name__main { display: block; font-size: 34px; letter-spacing: 1px; }
  .brand-name__sub { display: block; font-size: 14px; letter-spacing: 8.4px; margin-top: 4px; }

  .front__contact {
    position: absolute;
    left: 48px; top: 222px;
  }
  .person-name {
    font-weight: 600;
    font-size: 24px;
    color: var(--text-light);
    text-transform: uppercase;
    letter-spacing: 0.5px;
  }
  .person-roles {
    margin-top: 4px;
    font-size: 13px;
    color: var(--brand-green);
  }
  .phone-line {
    margin-top: 12px;
    display: flex; align-items: center; gap: 10px;
    font-size: 16px;
    color: var(--text-light);
  }
  .phone-line + .phone-line { margin-top: 4px; }
  .phone-line svg { width: 15px; height: 15px; fill: var(--brand-green); }

  /* back */
  .back__decor {
    position: absolute;
    left: 420px; top: 20px;
    width: 340px; height: 340px;
    border-radius: 50%;
    border: 26px solid rgba(255,255,255,0.05);
  }
  .back__brand {
    position: absolute;
    inset: 0;
    display: flex; align-items: center; justify-content: center; gap: 18px;
  }
  .brand-dot {
    width: 60px; height: 60px; border-radius: 50%;
    background: var(--card-dark);
    border: 5px solid var(--ring-light);
    flex: none;
  }
  .back__brand .brand-name__main { font-size: 40px; }
  .back__brand .brand-name__sub { font-size: 16px; letter-spacing: 9.6px; }
</style>
</head>
<body>
  <section class="card card--front">
    <div class="front__band"></div>
    <div class="front__emblem"></div>
    <div class="front__brand">
      <p class="brand-name">
        <span class="brand-name__main">Copper lark</span>
        <span class="brand-name__sub">buildworks</span>
      </p>
    </div>
    <div class="front__contact">
      <p class="person-name">Marcus Hale</p>
      <p class="person-roles">Licensed builder • Carpenter • Joiner</p>
      <p class="phone-line">
        <svg viewBox="0 0 24 24" aria-hidden="true"><path d="M6.6 10.8a15.1 15.1 0 0 0 6.6 6.6l2.2-2.2a1 1 0 0 1 1-.25 11.4 11.4 0 0 0 3.6.57 1 1 0 0 1 1 1V20a1 1 0 0 1-1 1A17 17 0 0 1 3 4a1 1 0 0 1 1-1h3.5a1 1 0 0 1 1 1c0 1.25.2 2.45.57 3.6a1 1 0 0 1-.25 1z"/></svg>
        0400 123 456
      </p>
      <p class="phone-line">
        <svg viewBox="0 0 24 24" aria-hidden="true"><path d="M6.6 10.8a15.1 15.1 0 0 0 6.6 6.6l2.2-2.2a1 1 0 0 1 1-.25 11.4 11.4 0 0 0 3.6.57 1 1 0 0 1 1 1V20a1 1 0 0 1-1 1A17 17 0 0 1 3 4a1 1 0 0 1 1-1h3.5a1 1 0 0 1 1 1c0 1.25.2 2.45.57 3.6a1 1 0 0 1-.25 1z"/></svg>
        5550 1234
      </p>
    </div>
  </section>

  <section class="card card--back">
    <div class="back__decor"></div>
    <div class="back__brand">
      <span class="brand-dot"></span>
      <p class="brand-name">
        <span class="brand-name__main">Copper lark</span>
        <span class="brand-name__sub">buildworks</span>
      </p>
    </div>
  </section>
</body>
</html>
```